Legal Service Estimated Retainer and Average Case Value

We need an 11x14 flyer that contains the standard retainers and average cost be case, both provided in documents, for each case type we handle. We need the information displayed, preferably in a way that makes the information readable but less troubling to a client shocked at price of litigation. We need one sheet with the retainers and average case value merged into one table.

Target Market(s)

Potential Clients

Font styles to use
Serif
Sans Serif

```html
<!DOCTYPE html>
<html lang="en">
<head>
<meta charset="utf-8">
<title>Legal Service Estimated Retainer &amp; Average Case Value</title>
<link rel="stylesheet" href="https://fonts.googleapis.com/css2?family=Cinzel:wght@400;500&family=Source+Sans+3:wght@400;600;700&display=swap">
<style>
  :root {
    --navy: #141a4a;
    --navy-mid: #262f7a;
    --royal: #1c4a9c;
    --ink: #1f3a93;
    --row-bg: #f2f2f3;
    --cell-grey: #e4e4e6;
    --rule: #5a62b0;
    --paper: #ffffff;
    --backdrop: #e9e9eb;
    --white: #ffffff;
  }
  * { margin: 0; padding: 0; box-sizing: border-box; }
  html, body { width: 1087px; height: 1200px; overflow: hidden; background: var(--backdrop); }
  .flyer {
    position: absolute; left: 72px; top: 0;
    width: 943px; height: 1200px;
    background: linear-gradient(180deg, #ffffff 0%, #f7f8fb 70%, #e6e9f1 100%);
    overflow: hidden;
  }
  .hero {
    position: absolute; left: 0; top: 0; width: 943px; height: 305px;
    background: linear-gradient(100deg, #4d55a0 0%, #3b4290 35%, #272e74 65%, #11163f 100%);
  }
  .hero-band { position: absolute; left: 0; top: 305px; width: 943px; height: 17px; background: var(--royal); }
  .brand {
    position: absolute; left: 60px; top: 148px; color: var(--white);
    font-family: "Cinzel", serif; line-height: 1;
  }
  .brand-pre { font-size: 10px; letter-spacing: 0.5px; display: block; margin-bottom: 3px; }
  .brand-name { font-size: 22px; letter-spacing: 0.5px; }
  .title {
    position: absolute; right: 50px; top: 98px; text-align: right;
    color: var(--white); font-family: "Cinzel", serif; font-weight: 500;
    font-size: 30px; line-height: 52px; letter-spacing: 1px;
  }
  .rates {
    position: absolute; left: 57px; top: 378px; width: 834px;
    border-collapse: collapse; font-family: "Source Sans 3", sans-serif;
    box-shadow: 0 2px 4px rgba(0,0,0,0.15);
  }
  .rates th {
    background: var(--royal); color: var(--white); font-family: "Cinzel", serif;
    font-weight: 400; height: 61px; font-size: 20px; letter-spacing: 0.5px;
    border-right: 2px solid var(--navy);
  }
  .rates th:first-child { text-align: left; padding-left: 17px; padding-top: 14px; border-radius: 6px 0 0 0; }
  .rates th.col-cost { font-size: 18px; padding-bottom: 8px; }
  .rates th.col-avg { font-size: 17px; line-height: 17px; border-right: none; border-radius: 0 6px 0 0; }
  .rates td {
    height: 50px; color: var(--ink); border-bottom: 1px solid var(--rule);
    border-right: 2px solid var(--rule);
  }
  .rates td.case { background: var(--row-bg); font-size: 16px; padding-left: 16px; width: 476px; padding-top: 6px; }
  .rates td.cost, .rates td.avg {
    background: var(--cell-grey); font-weight: 700; font-size: 17px; text-align: center; padding-top: 6px;
  }
  .rates td.cost { width: 175px; }
  .rates td.avg { width: 183px; border-right: none; white-space: nowrap; padding-left: 4px; }
  .rates tr:first-child td { height: 65px; padding-top: 18px; }
  .rates tr:last-child td { border-bottom: 2px solid var(--rule); }
  .paid { display: block; line-height: 15px; margin-top: -2px; }
  .footer { position: absolute; left: 0; bottom: 0; width: 943px; height: 36px; }
</style>
</head>
<body>
<main class="flyer">
  <header>
    <div class="hero" role="img" aria-label="Photo of two professionals shaking hands across a desk with documents, tinted navy"></div>
    <div class="hero-band"></div>
    <div class="brand"><span class="brand-pre">The Law Office of</span><span class="brand-name">Morgan T Ellison</span></div>
    <h1 class="title">Legal Service<br>Estimated Retainer &amp;<br>Average Case Value</h1>
  </header>

  <table class="rates">
    <thead>
      <tr>
        <th>Retainers and Total Estimated Case</th>
        <th class="col-cost">Costs</th>
        <th class="col-avg">Average Fee<br>Per Case Type</th>
      </tr>
    </thead>
    <tbody>
      <tr><td class="case">Divorce (3301 C): Retainer:</td><td class="cost">$2,000</td><td class="avg">$1,500 - $3,000</td></tr>
      <tr><td class="case">Divorce (3301 D): Retainer:</td><td class="cost">$2,500</td><td class="avg">$2,000 - $3,000</td></tr>
      <tr><td class="case">Divorce and Custody: Retainer:</td><td class="cost">$3,500</td><td class="avg">$5,000 - $8,000</td></tr>
      <tr><td class="case">Divorce and Equitable Distribution: Retainer:</td><td class="cost">$3,500</td><td class="avg">$6,000 - $10,000</td></tr>
      <tr><td class="case">Divorce and Support: Retainer:</td><td class="cost">$3,000</td><td class="avg">$5,000 - $8,000</td></tr>
      <tr><td class="case">Divorce, Custody and Support: Retainer:</td><td class="cost">$3,500</td><td class="avg">$8,000 - $12,000</td></tr>
      <tr><td class="case">Divorce, Equitable Distribution and Support: Retainer:</td><td class="cost">$3,500</td><td class="avg">$8,000 - $12,000</td></tr>
      <tr><td class="case">Divorce, Equitable Distribution and Custody: Retainer:</td><td class="cost">$5,000</td><td class="avg">$10,000 - $15,000</td></tr>
      <tr><td class="case">Divorce, Equitable Distribution, Custody and Support: Retainer:</td><td class="cost">$3,500</td><td class="avg">$12,000 - $15,000</td></tr>
      <tr><td class="case">Custody Initial Order: Retainer:</td><td class="cost">$3,000</td><td class="avg">$4,000 - $7,000</td></tr>
      <tr><td class="case">Custody Modification: Retainer:</td><td class="cost">$3,500</td><td class="avg">$5,000 - $8,000</td></tr>
      <tr><td class="case">Custody and Support: Retainer:</td><td class="cost">$3,000</td><td class="avg">$5,000 - $8,000</td></tr>
      <tr><td class="case">(PFA) Protection From Abuse:</td><td class="cost"><span class="paid">$2,000<br>Paid In Full</span></td><td class="avg">$1,500 - $3,000</td></tr>
    </tbody>
  </table>

  <svg class="footer" viewBox="0 0 943 36" preserveAspectRatio="none" aria-hidden="true">
    <defs>
      <linearGradient id="footerNavy" x1="0" x2="1" y1="0" y2="0">
        <stop offset="0" stop-color="#10143f"/>
        <stop offset="0.55" stop-color="#27308a"/>
        <stop offset="1" stop-color="#141a4a"/>
      </linearGradient>
    </defs>
    <polygon points="0,0 478,0 470,36 0,36" fill="url(#footerNavy)"/>
    <polygon points="482,0 943,0 943,36 474,36" fill="#1c4a9c"/>
  </svg>
</main>
</body>
</html>
```